Grafik für Software-Entwicklungsunternehmen gesucht
Zielgruppe
Stonmere ist ein Software-Entwicklungsunternehmen, welches die Applikation KOV7Site für Ihre Kunden betreibt und weiter entwickelt. Die Software arbeitet mit KI und augmendet reality uns ist technologisch führend. Alle weiteren Informationen in der PPT.
Aufgabenstellung
Wir brauchen in der Powerpoint-Präsentation eine super coole Grafik, welche die Hauptfunktionalitäten respektive der Prozess zeigt. Die Grafik muss in 3 Prozess-Schritten animiert werden können. Die Datei 'Prozessgrafik' muss als Grafik erstellt werden. Sollte das Budget für animierte Darstellung nicht ausreichen dann bitte melde. Evtl. führen wir den Auftrag dann weiter (Webseite/Kundenpräsentation)

```html
<!DOCTYPE html>
<html lang="de">
<head>
<meta charset="utf-8">
<title>Prozess – KOV7Site</title>
<link rel="stylesheet" href="https://fonts.googleapis.com/css2?family=Arimo:wght@400;700&display=swap">
<style>
  :root {
    --bg-deep: #020c0d;
    --bg-glow: #0d5a5c;
    --teal-bright: #2cc3c4;
    --teal-light: #63d4d3;
    --teal-core: #67c6cb;
    --white: #ffffff;
    --ink: #111111;
    --item-text: #f2ffff;
  }
  * { margin: 0; padding: 0; box-sizing: border-box; }
  html, body { width: 1200px; height: 675px; overflow: hidden; background: var(--bg-deep); }
  .canvas {
    position: relative;
    width: 1200px;
    height: 675px;
    overflow: hidden;
    font-family: "Arimo", Arial, sans-serif;
  }
  .backdrop {
    position: absolute;
    inset: 0;
    background:
      radial-gradient(ellipse 420px 330px at 600px 300px, rgba(40,190,190,0.55), transparent 70%),
      radial-gradient(ellipse 300px 380px at 1000px 420px, rgba(30,150,150,0.45), transparent 75%),
      radial-gradient(ellipse 260px 300px at 120px 380px, rgba(20,110,110,0.45), transparent 75%),
      linear-gradient(180deg, #031212 0%, var(--bg-glow) 50%, #031414 100%);
  }
  .shapes { position: absolute; inset: 0; width: 1200px; height: 675px; }
  .title {
    position: absolute;
    left: 52px;
    top: 48px;
    font-size: 38px;
    font-weight: 700;
    color: var(--white);
  }
  .centered { position: absolute; transform: translate(-50%, -50%); text-align: center; white-space: nowrap; }
  .step-title { font-size: 20px; font-weight: 700; color: var(--ink); line-height: 1.2; }
  .step-items { font-size: 12.5px; font-weight: 700; color: var(--item-text); line-height: 18.8px; }
  .product-name { font-size: 42px; font-weight: 700; color: var(--white); }
  .brand {
    position: absolute;
    left: 600px;
    top: 620px;
    transform: translateX(-50%);
    display: flex;
    align-items: center;
    gap: 8px;
    font-size: 19px;
    font-weight: 400;
    color: var(--white);
  }
  .brand-square { width: 14px; height: 14px; border: 2px solid var(--white); }
</style>
</head>
<body>
<main class="canvas">
  <div class="backdrop" role="img" aria-label="Dunkles türkisfarbenes Technologie-Bildmotiv: digitale Kreisschnittstelle, Sechsecke und eine Hand, die eine Oberfläche berührt"></div>

  <svg class="shapes" viewBox="0 0 1920 1080" aria-hidden="true">
    <defs>
      <clipPath id="above-band"><rect x="0" y="0" width="1920" height="478"/></clipPath>
      <clipPath id="below-band"><rect x="0" y="584" width="1920" height="496"/></clipPath>
      <g id="side-diamond">
        <polygon points="0,-322 322,0 0,322 -322,0" fill="#1a6e70" opacity="0.45"/>
        <polygon points="0,-267 267,0 0,267 -267,0" fill="var(--teal-bright)"/>
        <polygon points="0,-212 212,0 0,212 -212,0" fill="var(--teal-light)"/>
        <polygon points="0,-167 167,0 0,167 -167,0" fill="var(--white)"/>
      </g>
    </defs>

    <g clip-path="url(#above-band)">
      <use href="#side-diamond" x="428" y="522"/>
      <use href="#side-diamond" x="1507" y="522"/>
    </g>
    <g clip-path="url(#below-band)" opacity="0.42">
      <use href="#side-diamond" x="428" y="522"/>
      <use href="#side-diamond" x="1507" y="522"/>
    </g>

    <rect class="band" x="6" y="478" width="1914" height="106" fill="var(--white)"/>

    <polygon class="core-diamond" points="956,234 1244,522 956,810 668,522" fill="var(--teal-core)"/>
  </svg>

  <h1 class="title">Prozess</h1>

  <section class="step step-planning">
    <h2 class="centered step-title" style="left:263px; top:332px;">PLANUNG</h2>
    <p class="centered step-items" style="left:269px; top:400px;">Projekterfassung und Milestones<br>Schnittstellen-Management<br>BIM-Viewer</p>
  </section>

  <section class="step step-execution">
    <div class="centered product-name" style="left:600px; top:285px;">KOV7Site</div>
    <h2 class="centered step-title" style="left:597px; top:334px;">AUSFÜHRUNG</h2>
    <p class="centered step-items" style="left:599px; top:392px;">Intelligentes Baumanagement<br>Augmented reality<br>Künstlichen Intelligenz bei…</p>
  </section>

  <section class="step step-lifecycle">
    <h2 class="centered step-title" style="left:945px; top:333px;">LIFECYCLE-<br>MANAGEMENT</h2>
    <p class="centered step-items" style="left:947px; top:420px;">Facility-Management<br>Objekt-Abnahme<br>Garantieleistungen<br>Mängelbehebung<br>«Digitalisierung» Projekt-Owner</p>
  </section>

  <div class="brand"><span class="brand-square"></span><span>Stonmere</span></div>
</main>
</body>
</html>
```